Label Design for a New Alcoholized Root Beer

Create a design for a new alcoholized root beer. This is a new product category in the USA growing very rapidly. Root Beer is a popular flavor of Cola, but recently, beer manufacturers have added alcohol to it and have created a new product that has gained traction on the market at a tremendous rate.

Root Beer is vintage product that has been around for a hundred years. Consumers of this product are mostly male between the age of 30 to 45. They purchase this product for its nostalgia and vintage look and taste.

This product will be in a standard 355 mL brown bottle.

It is 5.9% abv.

The name of the product is ''Osric's Hard Root Beer''.

We have uploaded some pictures of traditional root beers to give you an idea of the feel we want our product to have and also, the bottle the product will be filled in.

Target Market(s)

Consumers are male 30-45, same market as craft beer consumers

Industry/Entity Type

Product

Requirements
Must have
• Design must have a vintage feel to it

```html
<!DOCTYPE html>
<html lang="en">
<head>
<meta charset="utf-8">
<title>Osric's Hard Root Beer — Label</title>
<link rel="stylesheet" href="https://fonts.googleapis.com/css2?family=Alfa+Slab+One&family=Oswald:wght@500&display=swap">
<style>
  :root {
    --backdrop: #5e5b5a;
    --paper: #d8caa2;
    --ribbon: #8c1d24;
    --ribbon-dark: #5e1016;
    --ink: #1c1f2e;
    --cream: #eadcb4;
  }
  html, body {
    margin: 0;
    padding: 0;
    width: 1200px;
    height: 900px;
    overflow: hidden;
    background: var(--backdrop);
  }
  .canvas {
    display: block;
    width: 1200px;
    height: 900px;
  }
  .label-body { fill: var(--paper); }
  .label-border { fill: none; stroke: var(--ribbon); stroke-width: 3; }
  .eyebrow {
    font-family: "Alfa Slab One", serif;
    font-size: 25px;
    letter-spacing: 3px;
    fill: var(--ink);
  }
  .eyebrow-rule { stroke: var(--ink); stroke-width: 6; stroke-linecap: round; }
  .brand-name {
    font-family: "Alfa Slab One", serif;
    font-size: 96px;
    fill: var(--ink);
  }
  .abv-seal { fill: var(--ribbon); }
  .abv-teeth { fill: none; stroke: var(--ribbon); stroke-width: 7; stroke-dasharray: 4 4; }
  .abv-text {
    font-family: "Oswald", sans-serif;
    font-weight: 500;
    font-size: 24px;
    letter-spacing: 1px;
    fill: var(--cream);
  }
  .ribbon { fill: var(--ribbon); }
  .ribbon-fold { fill: var(--ribbon-dark); }
  .ribbon-text {
    font-family: "Alfa Slab One", serif;
    fill: var(--cream);
    letter-spacing: 2px;
  }
  .volume {
    font-family: "Oswald", sans-serif;
    font-weight: 500;
    font-size: 32px;
    fill: var(--ink);
  }
  .origin {
    font-family: "Alfa Slab One", serif;
    font-size: 20px;
    letter-spacing: 2px;
    fill: var(--ink);
  }
</style>
</head>
<body>
<svg class="canvas" viewBox="0 0 1200 900" xmlns="http://www.w3.org/2000/svg">
  <g class="label">
    <path class="label-body" d="M332,258 Q600,216 868,258 A40,40 0 0 0 908,298 L908,668 A40,40 0 0 0 868,708 Q600,742 332,708 A40,40 0 0 0 292,668 L292,298 A40,40 0 0 0 332,258 Z"/>
    <path class="label-border" d="M343,270 Q600,229 857,270 A52,52 0 0 0 896,309 L896,657 A52,52 0 0 0 857,696 Q600,728 343,696 A52,52 0 0 0 304,657 L304,309 A52,52 0 0 0 343,270 Z"/>

    <g class="eyebrow-group">
      <line class="eyebrow-rule" x1="448" y1="291" x2="468" y2="291"/>
      <text class="eyebrow" x="600" y="300" text-anchor="middle">ORIGINAL</text>
      <line class="eyebrow-rule" x1="732" y1="291" x2="752" y2="291"/>
    </g>

    <g class="abv-badge">
      <circle class="abv-teeth" cx="373" cy="396" r="45"/>
      <circle class="abv-seal" cx="373" cy="396" r="44"/>
      <text class="abv-text" x="373" y="392" text-anchor="middle">5,9%</text>
      <text class="abv-text" x="373" y="420" text-anchor="middle">ABV</text>
    </g>

    <text class="brand-name" x="640" y="426" text-anchor="middle" textLength="370" lengthAdjust="spacingAndGlyphs">Osric's</text>

    <g class="ribbon-hard" transform="translate(0 16)">
      <path class="ribbon-fold" d="M488,470 L510,468 L505,528 Z"/>
      <path class="ribbon" d="M492,452 Q640,430 795,424 L790,486 Q650,494 500,520 Z"/>
      <text class="ribbon-text" font-size="50" x="645" y="494" text-anchor="middle" transform="rotate(-8 645 480)">HARD</text>
    </g>

    <g class="ribbon-root-beer">
      <path class="ribbon-fold" d="M845,500 L872,488 L866,548 Z"/>
      <path class="ribbon" d="M340,582 Q600,548 862,490 L870,546 Q610,594 346,632 Z"/>
      <path id="ribbon-curve" d="M368,620 Q610,580 858,528" fill="none"/>
      <text class="ribbon-text" font-size="52">
        <textPath href="#ribbon-curve" textLength="480" lengthAdjust="spacingAndGlyphs">ROOT BEER</textPath>
      </text>
    </g>

    <text class="volume" x="746" y="620" text-anchor="middle">355 ML</text>
    <text class="origin" x="600" y="688" text-anchor="middle">MADE IN USA</text>
  </g>
</svg>
</body>
</html>
```